Professional looking Roller Blind Discount Card that portrays quality at a value for money price!

We need a double sided business card designed as a discount card. Size 90mm wide x 55mm high.We would like it to look professional and portray quality at a value for money price point.I have uploaded a word document with a basic layout with the information we want included on each side of the card. Please put your own thought into the layout.

Contact Information for Business Card

As per word document attached.

```html
<!DOCTYPE html>
<html lang="en">
<head>
<meta charset="utf-8">
<title>Kestrel Projects – Roller Blind Discount Card</title>
<link rel="stylesheet" href="https://fonts.googleapis.com/css2?family=Arimo:wght@400;700&display=swap">
<style>
  :root {
    --page: #d6d6d6;
    --white: #ffffff;
    --blue: #29a8e0;
    --blue-light: #45b9ea;
    --grey: #6d6d6d;
    --grey-text: #757575;
    --brown: #7a6152;
    --brown-deep: #5e4a3f;
    --gold: #f2b01e;
    --gold-deep: #c98a0c;
  }
  * { box-sizing: border-box; margin: 0; padding: 0; }
  html, body {
    width: 1200px; height: 900px; overflow: hidden;
    background: var(--page);
    font-family: "Arimo", Arial, sans-serif;
  }
  .sheet {
    width: 1200px; height: 900px;
    display: flex; flex-direction: column; align-items: center; justify-content: center;
    gap: 40px;
  }
  .card {
    position: relative;
    width: 640px; height: 391px;
    overflow: hidden;
    box-shadow: 0 4px 14px rgba(0,0,0,.18);
  }

  /* ---------- Front: photo side ---------- */
  .card--front { background: var(--brown); }
  .front__photo {
    position: absolute; inset: 0;
    background: linear-gradient(135deg, #8a7463 0%, #b9c2b0 35%, #6f8f5a 60%, #a5ad98 80%, #6d5547 100%);
  }
  .front__brand-panel {
    position: absolute; left: 0; top: 0; width: 225px; height: 100%;
    background: rgba(94,74,63,.82);
    display: flex; flex-direction: column; align-items: center;
    padding-top: 38px; gap: 12px;
  }
  .brand {
    display: flex; align-items: center; gap: 8px;
    font-weight: 700; letter-spacing: .5px;
  }
  .brand__square { width: 14px; height: 14px; }
  .front__brand-panel .brand { color: var(--white); font-size: 17px; }
  .front__brand-panel .brand__square { background: var(--white); }
  .front__band {
    position: absolute; left: 225px; top: 0; right: 0; height: 130px;
    background: linear-gradient(90deg, var(--blue) 0%, var(--blue-light) 100%);
  }
  .front__title {
    position: absolute; left: 250px; top: 22px;
    background: var(--grey); color: var(--white);
    font-size: 34px; font-weight: 400; letter-spacing: 1px;
    padding: 6px 16px 5px;
  }
  .front__subtitle {
    position: absolute; left: 330px; top: 82px;
    color: var(--white); font-size: 24px;
  }
  .front__call-strip {
    position: absolute; right: 0; top: 130px; bottom: 0; width: 135px;
    background: rgba(94,74,63,.92);
  }
  .front__call {
    position: absolute; left: 50%; top: 50%;
    transform: translate(-50%, -50%) rotate(-90deg);
    white-space: nowrap; color: var(--white); text-align: center; line-height: 1.15;
  }
  .front__call-lead { font-size: 22px; letter-spacing: 1px; }
  .front__call-number { font-size: 30px; font-weight: 700; letter-spacing: 1px; }

  /* ---------- Back: offer side ---------- */
  .card--back { background: var(--white); }
  .back__rule { position: absolute; height: 3px; }
  .back__rule--blue { background: var(--blue); }
  .back__rule--grey { background: var(--grey); height: 7px; }
  .back__rule--tr-blue { left: 360px; right: 0; top: 52px; }
  .back__rule--tr-grey { left: 370px; right: 0; top: 60px; }
  .back__rule--bl-blue { left: 0; width: 270px; top: 322px; }
  .back__rule--bl-grey { left: 0; width: 260px; top: 330px; }
  .back__content {
    position: absolute; inset: 0;
    display: flex; flex-direction: column; align-items: center;
    padding-top: 96px; text-align: center;
  }
  .back__content .brand { color: var(--blue); font-size: 21px; }
  .back__content .brand__square { background: var(--blue); }
  .back__offer {
    color: var(--blue); font-size: 36px; font-weight: 700; margin-top: 14px;
  }
  .back__line { color: var(--grey-text); font-size: 19px; line-height: 1.25; }
  .back__badges { display: flex; gap: 22px; margin: 12px 0 10px; }
  .back__call { color: var(--grey-text); font-size: 20px; }
  .back__call strong { color: var(--blue); font-weight: 700; }
</style>
</head>
<body>
<main class="sheet">

  <section class="card card--front" aria-label="Card front">
    <div class="front__photo" role="img" aria-label="Photo of a room with roller blinds over large windows looking onto a garden"></div>
    <div class="front__brand-panel">
      <div class="brand"><span class="brand__square"></span>KESTREL PROJECTS</div>
    </div>
    <div class="front__band"></div>
    <h1 class="front__title">ROLLER BLINDS</h1>
    <p class="front__subtitle">Huge Selection of Fabrics</p>
    <div class="front__call-strip">
      <div class="front__call">
        <div class="front__call-lead">CALL TODAY!</div>
        <div class="front__call-number">0400 527 193</div>
      </div>
    </div>
  </section>

  <section class="card card--back" aria-label="Card back">
    <div class="back__rule back__rule--blue back__rule--tr-blue"></div>
    <div class="back__rule back__rule--grey back__rule--tr-grey"></div>
    <div class="back__rule back__rule--blue back__rule--bl-blue"></div>
    <div class="back__rule back__rule--grey back__rule--bl-grey"></div>
    <div class="back__content">
      <div class="brand"><span class="brand__square"></span>KESTREL PROJECTS</div>
      <p class="back__offer">25% OFF</p>
      <p class="back__line">Quality Custom Made Roller Blinds</p>
      <p class="back__line">Blockout • Screen • Light Filtering</p>
      <div class="back__badges" aria-label="Guarantee badges">
        <svg width="40" height="40" viewBox="0 0 40 40"><circle cx="20" cy="20" r="19" fill="var(--gold-deep)"/><circle cx="20" cy="20" r="15" fill="var(--gold)"/></svg>
        <svg width="40" height="40" viewBox="0 0 40 40"><circle cx="20" cy="20" r="19" fill="var(--gold-deep)"/><circle cx="20" cy="20" r="15" fill="var(--gold)"/></svg>
        <svg width="40" height="40" viewBox="0 0 40 40"><circle cx="20" cy="20" r="19" fill="var(--gold-deep)"/><circle cx="20" cy="20" r="15" fill="var(--gold)"/></svg>
      </div>
      <p class="back__call">Call <strong>0400 527 193</strong> Today!</p>
    </div>
  </section>

</main>
</body>
</html>
```